A Must Standout Business Card Design

I need A card that stands out from the rest. Possibly raised letters or Metallic card, Shiny or glossy, Looking for a more modern look or something throwback design would be nice. So i'm a open to different designs. I have a logo but not to happy with it. I will send it on a sample business card I do like.I might like you to tweak the designed card I am sending you. A new logo may be in order too. Make logo something that can be engraved on metal. I was thinking possibly KW in a box or KW mirror image or Backward E then a forward B in a circle. The name of my company is Korvath Works Inc. I designed an innovative hand tool to remove Valve Cores. I call the tool the Stem Pin Clutcher. My tool grips and holds onto valve cores like no other tool does. Check it out at my website pinstemhandy.com Maybe put a picture of the tool on the card raised or embossed or that spot gloss.
Updates
Everybody I must say have sent over some awesome designs! Every submission has been my favorite so I will be making my decision after the deadline. Nice work everyone!
Target Market(s)
Automotive people, People who wholesale refrigeration parts and equipment, People who use tools
Industry/Entity Type
Business
Contact Information for Business Card
Korvath Works Inc., 4827 Foxhollow Ln. Unit C Harlow Falls IL 60912, Dale Minton President, 708-555-0187, Pinstemhandy.com, Logo
Look and feel
Each slider illustrates characteristics of the customer's brand and the style your logo design should communicate.

```html
<!DOCTYPE html>
<html lang="en">
<head>
<meta charset="utf-8">
<title>Korvath Works Inc — Business Card</title>
<link rel="stylesheet" href="https://fonts.googleapis.com/css2?family=Aldrich&display=swap">
<style>
  :root {
    --bg: #ffffff;
    --gold-dark: #a8803f;
    --gold-mid: #d6ab55;
    --gold-light: #f9e08e;
    --gold-text: #9a7639;
    --silver-dark: #bdbdbd;
    --silver-light: #fbfbfb;
    --grey-text: #8c8c8e;
    --shadow: rgba(0,0,0,.35);
  }
  html, body { margin: 0; padding: 0; width: 1200px; height: 1000px; overflow: hidden; background: var(--bg); }
  body { position: relative; font-family: "Aldrich", sans-serif; }
  .gold {
    background: linear-gradient(100deg, var(--gold-dark) 0%, var(--gold-mid) 25%, var(--gold-light) 48%, var(--gold-mid) 70%, var(--gold-dark) 100%);
  }
  .wordmark {
    position: absolute; left: 720px; top: 206px; width: 388px; text-align: center;
    font-size: 30px; line-height: 40px; color: var(--gold-text); letter-spacing: 1px;
  }
  .screw { position: absolute; }
  .card {
    position: absolute; left: 270px; top: 398px; width: 576px; height: 327px;
    background: linear-gradient(120deg, var(--silver-dark) 0%, #e6e6e6 35%, var(--silver-light) 55%, #dcdcdc 75%, var(--silver-dark) 100%);
    border: 3px solid #d0d0d0; box-sizing: border-box;
    box-shadow: 5px 6px 7px var(--shadow);
  }
  .card-band {
    position: absolute; left: 4px; top: 14px; width: 561px; height: 72px;
  }
  .company-name {
    position: absolute; left: 66px; top: 18px; font-size: 31px; line-height: 38px;
    color: var(--gold-text); letter-spacing: 1px;
  }
  .address, .person, .phone { position: absolute; color: var(--grey-text); margin: 0; white-space: nowrap; }
  .address { left: 40px; top: 110px; font-size: 21px; line-height: 26px; letter-spacing: 1px; }
  .person { left: 47px; top: 192px; font-size: 26px; letter-spacing: 1.5px; }
  .phone { left: 170px; top: 246px; font-size: 22px; letter-spacing: 2px; }
  .web-plate {
    position: absolute; left: 117px; top: 274px; width: 323px; height: 40px;
    border: 1px solid #c99f4e; box-sizing: border-box;
  }
  .web-plate .url {
    position: absolute; left: 0; right: 0; top: 7px; text-align: center;
    font-size: 21px; color: var(--gold-text); letter-spacing: 1px;
  }
  .tool-art {
    position: absolute; left: 450px; top: 32px; width: 74px; height: 272px;
    border-radius: 30px 30px 6px 6px;
    background: linear-gradient(90deg, #b8b8b8, #f1f1f1 50%, #9e9e9e);
    opacity: .85;
  }
</style>
</head>
<body>
<svg width="0" height="0" style="position:absolute">
  <defs>
    <radialGradient id="screwGold" cx="40%" cy="35%" r="70%">
      <stop offset="0" stop-color="#f9e08e"/><stop offset="1" stop-color="#b48638"/>
    </radialGradient>
    <symbol id="screw-head" viewBox="0 0 32 32">
      <circle cx="16" cy="16" r="15" fill="url(#screwGold)" stroke="#a8803f" stroke-width="1"/>
      <path d="M13 7h6v6h6v6h-6v6h-6v-6H7v-6h6z" fill="none" stroke="#a8803f" stroke-width="1.4"/>
    </symbol>
    <symbol id="screw-ring" viewBox="0 0 36 36">
      <circle cx="18" cy="18" r="17" fill="#f2f2f2" stroke="#bcbcbc"/>
      <use href="#screw-head" x="3" y="3" width="30" height="30"/>
    </symbol>
  </defs>
</svg>

<div class="wordmark">Korvath Works Inc</div>

<div class="card">
  <div class="card-band gold">
    <div class="company-name">Korvath Works Inc</div>
  </div>
  <div class="tool-art" role="img" aria-label="Silver knurled valve core hand tool on a key ring"></div>
  <p class="address">4827 Foxhollow Ln. Unit C<br>Harlow Falls IL 60912</p>
  <p class="person">Dale Minton President</p>
  <p class="phone">708-555-0187</p>
  <div class="web-plate gold">
    <svg class="screw" style="left:13px;top:14px" width="11" height="11"><use href="#screw-head"/></svg>
    <div class="url">Pinstemhandy.com</div>
    <svg class="screw" style="left:297px;top:14px" width="11" height="11"><use href="#screw-head"/></svg>
  </div>
  <svg class="screw" style="left:14px;top:278px" width="36" height="36"><use href="#screw-ring"/></svg>
  <svg class="screw" style="left:521px;top:278px" width="36" height="36"><use href="#screw-ring"/></svg>
</div>
</body>
</html>
```